Private Maths Tuition Flyer based in London

I am opening up a new Maths tuition centre in North West London. The flyer will be delivered to over 8,000 homes within the immediate vicinity. The design should be suitable to be printed on an A5 sheet and read in a portrait orientation.

The flyer should include the following:

The headline statement should be "Private Maths Tuition"

Secondary headline statement is the following "GCSE, A-Levels, 11 Plus exams"

Some of service offerings/selling points are:

- Free first session
- Monthly Feedback reports
- Free support outside of sessions
- Clear Target grades
- Personalised Lesson plans
- Tangible Results

Another statement that should be featured is "Book your free session by visiting www.lernova.co.uk" or something similar to that.

"Contact Details:
020 4719 8263
enquiries@lernova.co.uk"

"Address:
Kelbridge Business and Innovation Centre
Ashvale Court
Wrenfield Road
HA4 9QD"

Attached you'll see a logo which should be included and also a map of where we are. I am open to new images for the map if you guys have any, rather than a screen shot from google maps but it should be clear to see.

I would like the content above to be displayed in a clear and concise manner that is easy to read. You have creative license on where this information should be displayed and where the images should be but on the whole it should look aesthetically pleasing on the eye.

Target Market(s)

Students, Parents. Parents who want maths tutors.

Industry/Entity Type

Tutoring

Font styles to use
Sans Serif

Requirements
Must have
• *logo*
• Private Maths Tuition
• GCSE, A-Levels, 11 Plus exams
• - Free first session
• - Monthly Feedback reports
• - Free support outside of sessions
• - Clear Target grades
• - Personalised Lesson plans
• - Tangible Results
• Book your free session by visiting www.lernova.co.uk" or something similar to that.
• Contact Details:
• 020 4719 8263
• enquiries@lernova.co.uk
• Address (*with map*):
• Kelbridge Business and Innovation Centre
• Ashvale Court
• Wrenfield Road
• HA4 9QD
Nice to have
• similar colour scheme as the logo. creative background design.

```html
<!DOCTYPE html>
<html lang="en">
<head>
<meta charset="utf-8">
<title>Lernova – Private Maths Tuition Flyer</title>
<link rel="stylesheet" href="https://fonts.googleapis.com/css2?family=Oswald:wght@500;700&family=Open+Sans:ital,wght@0,400;0,600;0,700;1,600;1,700&display=swap">
<style>
  :root{
    --blue:#1a5fa8;
    --blue-dark:#124a86;
    --orange:#f07a1a;
    --green:#3aa54a;
    --ink:#1d2a3a;
    --white:#ffffff;
    --paper:#f4f6f8;
  }
  *{box-sizing:border-box;margin:0;padding:0}
  html,body{width:900px;height:1200px;overflow:hidden;background:var(--paper)}
  .flyer{position:relative;width:900px;height:1200px;background:var(--white);font-family:"Open Sans",Arial,sans-serif;color:var(--ink);overflow:hidden}
  .hero-photo{position:absolute;left:0;top:0;width:900px;height:560px;
    background:linear-gradient(180deg,#e9edf1 0%,#d4dbe3 55%,#bfc9d4 100%)}
  .chevron{position:absolute;left:0;top:470px;width:900px;height:170px}
  .brand{position:absolute;left:60px;top:640px;display:flex;align-items:center;gap:12px}
  .brand-dot{width:34px;height:34px;border-radius:50%;background:var(--green)}
  .brand-name{font-family:"Open Sans",Arial,sans-serif;font-weight:700;font-size:46px;color:var(--orange);letter-spacing:.5px}
  .headline{position:absolute;left:40px;top:712px;width:420px;font-family:"Oswald",Arial,sans-serif;font-weight:700;text-transform:uppercase;line-height:1.05}
  .headline .main{display:block;color:var(--blue);font-size:38px}
  .headline .sub{display:block;color:var(--orange);font-size:40px;margin-top:4px}
  .book-btn{position:absolute;left:40px;top:860px;width:400px;height:46px;background:var(--green);color:var(--white);
    font-family:"Oswald",Arial,sans-serif;font-weight:500;font-size:26px;text-transform:uppercase;display:flex;align-items:center;justify-content:center;letter-spacing:.5px}
  .book-text{position:absolute;left:40px;top:912px;width:400px;text-align:center;line-height:1.2}
  .book-text .by{display:block;font-size:24px;font-weight:600;color:var(--blue)}
  .book-text .url{display:block;font-size:30px;font-weight:700;color:var(--ink)}
  .contact-bar{position:absolute;left:40px;top:1000px;width:400px;height:38px;background:var(--blue);color:var(--white);
    font-weight:700;font-size:22px;display:flex;align-items:center;justify-content:center}
  .contact-list{position:absolute;left:60px;top:1048px;list-style:none;font-size:15px;color:var(--ink)}
  .contact-list li{display:flex;align-items:flex-start;gap:10px;margin-bottom:6px;line-height:1.3}
  .contact-list .big{font-size:19px;font-weight:600}
  .contact-list svg{flex:none;margin-top:2px}
  .offers-panel{position:absolute;left:485px;top:612px;width:415px;height:528px;background:var(--blue)}
  .free-tab{position:absolute;left:505px;top:640px;width:265px;height:40px;background:var(--orange);color:var(--white);
    font-family:"Oswald",Arial,sans-serif;font-weight:500;font-size:24px;text-transform:uppercase;display:flex;align-items:center;justify-content:center}
  .offers-title{position:absolute;left:525px;top:700px;color:var(--white);font-family:"Oswald",Arial,sans-serif;font-weight:500;font-size:26px;text-transform:uppercase}
  .offers-rule{position:absolute;left:525px;top:740px;width:190px;height:2px;background:var(--white)}
  .offers-list{position:absolute;left:525px;top:756px;list-style:none;color:var(--white);font-style:italic;font-weight:600;font-size:17px}
  .offers-list li{display:flex;align-items:center;gap:10px;margin-bottom:7px}
  .offers-list li::before{content:"";width:8px;height:8px;background:var(--orange);flex:none}
  .map{position:absolute;left:505px;top:930px;width:375px;height:190px;border:3px solid var(--white);
    background:linear-gradient(135deg,#e6eee2 0%,#d5e2cf 50%,#c7d8c2 100%)}
  .footer-band{position:absolute;left:0;top:1150px;width:900px;height:50px}
</style>
</head>
<body>
<div class="flyer">
  <div class="hero-photo" role="img" aria-label="Photo of smiling students holding books and folders, one giving a thumbs up"></div>

  <svg class="chevron" viewBox="0 0 900 170" aria-hidden="true">
    <polygon points="0,30 450,110 900,30 900,170 0,170" fill="var(--white)"/>
    <polygon points="0,10 450,90 900,10 900,30 450,110 0,30" fill="var(--blue)"/>
    <polygon points="0,0 450,80 900,0 900,10 450,90 0,10" fill="var(--orange)"/>
    <polygon points="0,40 450,120 900,40 900,48 450,128 0,48" fill="var(--orange)"/>
  </svg>

  <div class="brand">
    <span class="brand-dot"></span>
    <span class="brand-name">Lernova</span>
  </div>

  <h1 class="headline">
    <span class="main">Private Maths Tuition</span>
    <span class="sub">GCSE, A-Levels, 11 Plus Exams</span>
  </h1>

  <div class="book-btn">Book your free session</div>
  <p class="book-text"><span class="by">by visiting</span><span class="url">www.lernova.co.uk</span></p>

  <div class="contact-bar">Contact Details</div>
  <ul class="contact-list">
    <li class="big">
      <svg width="18" height="18" viewBox="0 0 24 24"><path fill="#1a5fa8" d="M6.6 10.8a15 15 0 0 0 6.6 6.6l2.2-2.2c.3-.3.7-.4 1-.2 1.1.4 2.3.6 3.6.6.6 0 1 .4 1 1V20c0 .6-.4 1-1 1A17 17 0 0 1 3 4c0-.6.4-1 1-1h3.5c.6 0 1 .4 1 1 0 1.3.2 2.5.6 3.6.1.3 0 .7-.2 1z"/></svg>
      020 4719 8263
    </li>
    <li>
      <svg width="18" height="14" viewBox="0 0 24 18"><rect x="1" y="1" width="22" height="16" fill="none" stroke="#1a5fa8" stroke-width="2"/><path d="M1 1l11 9 11-9" fill="none" stroke="#1a5fa8" stroke-width="2"/></svg>
      enquiries@lernova.co.uk
    </li>
    <li>
      <svg width="16" height="20" viewBox="0 0 24 30"><path fill="#1a5fa8" d="M12 0a10 10 0 0 0-10 10c0 7.5 10 20 10 20s10-12.5 10-20A10 10 0 0 0 12 0zm0 14a4 4 0 1 1 0-8 4 4 0 0 1 0 8z"/></svg>
      <span>Kelbridge Business and Innovation Centre<br>Ashvale Court, Wrenfield Road, HA4 9QD</span>
    </li>
  </ul>

  <div class="offers-panel"></div>
  <div class="free-tab">Free first session</div>
  <h2 class="offers-title">Other Offers</h2>
  <div class="offers-rule"></div>
  <ul class="offers-list">
    <li>Monthly Feedback reports</li>
    <li>Free support outside of sessions</li>
    <li>Clear Target grades</li>
    <li>Personalised Lesson plans</li>
    <li>Tangible Results</li>
  </ul>
  <div class="map" role="img" aria-label="Street map showing the location of Kelbridge Business and Innovation Centre"></div>

  <svg class="footer-band" viewBox="0 0 900 50" preserveAspectRatio="none" aria-hidden="true">
    <rect width="900" height="50" fill="var(--blue)"/>
    <rect width="900" height="14" fill="var(--orange)"/>
  </svg>
</div>
</body>
</html>
```